Velmora Biz Card 2019

New business card for Velmora Property Inspections. We are a residential home inspection company in Arizona.

Target Market(s)

Real Estate

Font styles to use
Sans Serif

Requirements
Must have
• Glen Mirewick
• Home Inspector
• Velmora Property Inspections, LLC
• 480-555-0172
• glen@velmora-llc.example

```html
<!DOCTYPE html>
<html lang="en">
<head>
<meta charset="utf-8">
<title>Velmora Business Card</title>
<link rel="stylesheet" href="https://fonts.googleapis.com/css2?family=Poppins:wght@300;400;500;600&display=swap">
<style>
  :root {
    --green: #4cb848;
    --grey: #7d7f82;
    --grey-light: #b9bbbd;
    --ink: #3a3a3a;
    --white: #ffffff;
    --backdrop: #eef0ee;
  }
  * { box-sizing: border-box; margin: 0; padding: 0; }
  html, body { width: 1200px; height: 870px; overflow: hidden; }
  body {
    background: var(--backdrop);
    font-family: "Poppins", sans-serif;
    position: relative;
  }
  .card {
    position: absolute;
    top: 280px;
    width: 540px;
    height: 310px;
    border-radius: 16px;
    overflow: hidden;
    box-shadow: 0 6px 22px rgba(0,0,0,0.14);
  }
  .card--front { left: 44px; background: var(--white); }
  .card--back { left: 616px; background: var(--green); }

  .front-waves { position: absolute; inset: 0; }

  .portrait {
    position: absolute;
    left: 26px; top: 24px;
    width: 82px; height: 82px;
    border: 2px solid var(--green);
    padding: 4px;
    background: var(--white);
  }
  .portrait-fill {
    width: 100%; height: 100%;
    background: linear-gradient(180deg, #c9ced3 0%, #8d949b 55%, #2f3236 100%);
  }
  .identity { position: absolute; left: 108px; top: 34px; }
  .identity-rule {
    position: absolute; left: 0; top: 12px;
    width: 20px; height: 2px; background: var(--green);
  }
  .identity-name {
    margin-left: 26px;
    font-size: 17px; font-weight: 600; line-height: 24px;
    color: var(--green); letter-spacing: 0.3px;
    text-transform: uppercase;
  }
  .identity-title {
    margin-left: 26px;
    font-size: 12px; font-weight: 400; color: var(--ink);
  }

  .brand {
    position: absolute;
    display: flex; align-items: center; gap: 10px;
    font-weight: 600; letter-spacing: 1px;
  }
  .brand-mark { display: block; }
  .brand--front { right: 34px; top: 66px; font-size: 32px; color: var(--grey); }
  .brand--front .brand-mark { width: 22px; height: 22px; background: var(--green); }
  .brand--back {
    left: 50%; top: 50%; transform: translate(-50%, -50%);
    font-size: 40px; color: var(--white);
  }
  .brand--back .brand-mark { width: 28px; height: 28px; border-radius: 50%; background: var(--white); }

  .contact-list {
    position: absolute; left: 26px; top: 202px;
    list-style: none;
  }
  .contact-item {
    display: flex; align-items: center; gap: 9px;
    height: 21px;
    font-size: 12px; font-weight: 300; color: var(--white);
  }
  .contact-icon { width: 13px; height: 13px; flex: none; }

  .address {
    position: absolute; right: 30px; top: 226px;
    text-align: right;
    font-size: 12px; font-weight: 300; color: var(--white);
    line-height: 19px;
    font-style: normal;
  }
  .address-company { font-weight: 500; }
</style>
</head>
<body>

<section class="card card--front" aria-label="Business card front">
  <svg class="front-waves" width="540" height="310" viewBox="0 0 540 310">
    <path d="M0,178 C150,146 340,214 540,160 L540,310 L0,310 Z" fill="var(--green)"/>
    <path d="M0,162 C150,130 340,198 540,144" fill="none" stroke="var(--grey-light)" stroke-width="7"/>
    <path d="M0,150 C150,118 340,186 540,132" fill="none" stroke="var(--green)" stroke-width="2.5"/>
  </svg>

  <div class="portrait">
    <div class="portrait-fill" role="img" aria-label="Portrait photo of Glen Mirewick"></div>
  </div>

  <div class="identity">
    <span class="identity-rule"></span>
    <p class="identity-name">Glen Mirewick</p>
    <p class="identity-title">Home Inspector</p>
  </div>

  <div class="brand brand--front">
    <span class="brand-mark"></span>
    <span class="brand-name">VELMORA</span>
  </div>

  <ul class="contact-list">
    <li class="contact-item">
      <svg class="contact-icon" viewBox="0 0 14 14"><circle cx="7" cy="7" r="7" fill="var(--white)"/><path d="M4.5,3.5 l1.5,0 0.6,2 -0.9,0.7 a5,5 0 0 0 2.1,2.1 l0.7,-0.9 2,0.6 0,1.5 a1,1 0 0 1 -1,1 a6,6 0 0 1 -6,-6 a1,1 0 0 1 1,-1z" fill="var(--green)"/></svg>
      480-555-0172
    </li>
    <li class="contact-item">
      <svg class="contact-icon" viewBox="0 0 14 14"><circle cx="7" cy="7" r="7" fill="var(--white)"/><path d="M4.5,3.5 l1.5,0 0.6,2 -0.9,0.7 a5,5 0 0 0 2.1,2.1 l0.7,-0.9 2,0.6 0,1.5 a1,1 0 0 1 -1,1 a6,6 0 0 1 -6,-6 a1,1 0 0 1 1,-1z" fill="var(--green)"/></svg>
      (619) 555-0193
    </li>
    <li class="contact-item">
      <svg class="contact-icon" viewBox="0 0 14 14"><circle cx="7" cy="7" r="7" fill="var(--white)"/><rect x="3.5" y="4.5" width="7" height="5" fill="none" stroke="var(--green)" stroke-width="1"/><path d="M3.5,4.5 L7,7.3 L10.5,4.5" fill="none" stroke="var(--green)" stroke-width="1"/></svg>
      glen@velmora-llc.example
    </li>
    <li class="contact-item">
      <svg class="contact-icon" viewBox="0 0 14 14"><circle cx="7" cy="7" r="7" fill="var(--white)"/><circle cx="7" cy="7" r="3.6" fill="none" stroke="var(--green)" stroke-width="1"/><ellipse cx="7" cy="7" rx="1.5" ry="3.6" fill="none" stroke="var(--green)" stroke-width="0.9"/><line x1="3.4" y1="7" x2="10.6" y2="7" stroke="var(--green)" stroke-width="0.9"/></svg>
      www.velmora-llc.example
    </li>
  </ul>

  <address class="address">
    <span class="address-company">Velmora Property Inspections, LLC</span><br>
    4180 Larkspur Lane<br>
    Mesa Vista, AZ 85299
  </address>
</section>

<section class="card card--back" aria-label="Business card back">
  <div class="brand brand--back">
    <span class="brand-mark"></span>
    <span class="brand-name">VELMORA</span>
  </div>
</section>

</body>
</html>
```